Lumen Path - Fiber Internet to the home postcard

Design a postcard for my company, Lumen Path, using the logo below. On the front of the card:
- No Buffering • No BS
- Second line should be the logo
- $60 / month • 10-Gigs
- lumenpath.net

Color palate should follow the colors in the logo.

Address should say
- Special pricing during construction
- Our best price
- Our fastest speed
- $60 / month • 10-Gigs
- lumenpath.net

Target Market(s)

25 - 55 year olds. Middle income/class. People with kids and pick up trucks

Industry/Entity Type

Fiber Internet Service Provider

Font styles to use
Sans Serif

Colors

Designer to choose colors to be used in the design.

Requirements
Nice to have
• I am open to more creative changes

```html
<!DOCTYPE html>
<html lang="en">
<head>
<meta charset="utf-8">
<title>Lumen Path – Fiber Postcard</title>
<link rel="stylesheet" href="https://fonts.googleapis.com/css2?family=Barlow:wght@500;600;700;800&display=swap">
<style>
  :root {
    --green: #7ac143;
    --green-dark: #4f8a24;
    --green-deep: #2e5a16;
    --navy: #002a5c;
    --white: #ffffff;
    --page: #ffffff;
  }
  * { box-sizing: border-box; margin: 0; padding: 0; }
  html, body { width: 906px; height: 1200px; overflow: hidden; background: var(--page); }
  body { position: relative; font-family: "Barlow", Arial, sans-serif; }

  .card { position: absolute; left: 148px; width: 604px; height: 431px; background: var(--green); overflow: hidden; }
  .card--front { top: 146px; }
  .card--back { top: 616px; }
  .abs { position: absolute; }

  /* Front */
  .tagline { top: 0; left: 0; width: 604px; height: 80px; }
  .tagline__text { position: absolute; top: 14px; color: var(--navy); font-weight: 800; font-size: 46px; line-height: 1; letter-spacing: .5px; white-space: nowrap; }
  .tagline__text small { font-size: 31px; font-weight: 800; margin-right: 7px; }
  .brand-band { top: 80px; left: 0; width: 604px; height: 144px; background: var(--navy); }
  .brand-band__name { position: absolute; left: 86px; top: 38px; color: var(--white); font-weight: 800; font-size: 62px; line-height: 1; letter-spacing: -.5px; white-space: nowrap; }
  .brand-band__dot { position: absolute; left: 442px; top: 10px; width: 124px; height: 124px; border-radius: 50%; background: var(--green); }

  /* Offer boxes */
  .offer { width: 164px; height: 118px; border: 5px solid var(--navy); border-radius: 16px; display: flex; flex-direction: column; align-items: center; justify-content: center; color: var(--white); font-weight: 700; line-height: .92; text-shadow: 2px 2px 0 var(--green-dark); }
  .offer__big { font-size: 48px; }
  .offer__small { font-size: 37px; }
  .mascot { width: 110px; background: linear-gradient(180deg, #1b2d5e 0%, #1b2d5e 30%, #ffffff 31%, #8ac85a 100%); opacity: .9; border-radius: 40px 40px 4px 4px; }

  /* CTA */
  .cta { left: 36px; width: 534px; height: 42px; }
  .cta__url { position: absolute; left: 276px; top: 0; width: 258px; height: 42px; background: var(--white); border-radius: 0 21px 21px 0; color: var(--navy); font-weight: 800; font-size: 22px; line-height: 42px; padding-left: 27px; }
  .cta__button { position: absolute; left: 0; top: 0; width: 288px; height: 42px; background: var(--navy); border-radius: 21px; color: var(--white); font-weight: 800; font-size: 27px; line-height: 42px; text-align: center; letter-spacing: .5px; }

  /* Back */
  .back-panel { top: 0; left: 0; }
  .feature { color: var(--white); font-weight: 600; font-size: 25px; line-height: 29px; white-space: nowrap; }
  .feature b { font-weight: 800; }
  .feature--caps { font-weight: 800; }
  .homes { left: 474px; top: 52px; width: 116px; height: 62px; border-radius: 8px; background: linear-gradient(160deg, var(--green-deep) 0%, #3d7420 55%, #5e9e31 100%); }
  .brand-small { left: 418px; top: 128px; height: 44px; display: flex; align-items: center; gap: 6px; white-space: nowrap; }
  .brand-small__name { color: var(--white); font-weight: 800; font-size: 24px; line-height: 1; }
  .brand-small__dot { flex: none; width: 38px; height: 38px; border-radius: 50%; background: var(--navy); }
</style>
</head>
<body>

<!-- Front of postcard -->
<section class="card card--front">
  <div class="abs tagline">
    <svg class="abs" style="left:34px;top:22px" width="38" height="38" viewBox="0 0 38 38" aria-hidden="true">
      <circle cx="19" cy="19" r="16" fill="none" stroke="#fff" stroke-width="3" stroke-dasharray="3 3.3"/>
      <path d="M15 12 L26 19 L15 26 Z" fill="#fff"/>
    </svg>
    <p class="tagline__text" style="left:86px"><small>NO</small>BUFFERING</p>
    <svg class="abs" style="left:404px;top:22px" width="38" height="38" viewBox="0 0 38 38" aria-hidden="true">
      <circle cx="19" cy="19" r="16.5" fill="none" stroke="#fff" stroke-width="2.5"/>
      <path d="M13 26 V15 M17 25 V11 M21 25 V11 M25 25 V14 M13 26 Q19 31 26 26" fill="none" stroke="#fff" stroke-width="2" stroke-linecap="round"/>
      <line x1="8" y1="8" x2="30" y2="30" stroke="#fff" stroke-width="2.5"/>
    </svg>
    <p class="tagline__text" style="left:454px"><small>NO</small>BS</p>
  </div>

  <div class="abs brand-band">
    <span class="brand-band__name">Lumen Path</span>
    <span class="brand-band__dot"></span>
  </div>

  <div class="abs offer" style="left:68px;top:240px"><span class="offer__big">$60/</span><span class="offer__small">MONTH</span></div>
  <div class="abs mascot" role="img" aria-label="Cartoon character with arms raised holding wifi signals" style="left:249px;top:238px;height:131px"></div>
  <div class="abs offer" style="left:373px;top:240px"><span class="offer__big">10</span><span class="offer__small">GIGS</span></div>

  <div class="abs cta" style="top:369px">
    <span class="cta__url">lumenpath.net</span>
    <span class="cta__button">SIGN UP TODAY!</span>
  </div>
</section>

<!-- Address side of postcard -->
<section class="card card--back">
  <svg class="abs back-panel" width="604" height="184" viewBox="0 0 604 184" aria-hidden="true">
    <polygon points="0,0 513,0 380,184 0,184" fill="#002a5c"/>
    <line x1="220" y1="21" x2="220" y2="85" stroke="#0d3a70" stroke-width="1.5"/>
    <line x1="17" y1="104" x2="410" y2="104" stroke="#0d3a70" stroke-width="1.5"/>
  </svg>

  <svg class="abs" style="left:38px;top:44px" width="38" height="38" viewBox="0 0 38 38" aria-hidden="true">
    <path d="M4 18 H11 V34 H4 Z M11 19 L18 9 Q19 3 23 5 Q25 8 22 16 H32 Q35 17 34 21 L31 32 Q30 34 27 34 H11" fill="none" stroke="#7ac143" stroke-width="2.6" stroke-linejoin="round"/>
  </svg>
  <p class="abs feature" style="left:86px;top:31px"><b>Our BEST</b><br>Price</p>

  <svg class="abs" style="left:232px;top:37px" width="58" height="50" viewBox="0 0 58 50" aria-hidden="true">
    <path d="M8 40 A22 22 0 1 1 50 40" fill="none" stroke="#7ac143" stroke-width="2.6"/>
    <path d="M14 36 A16 16 0 1 1 44 36" fill="none" stroke="#7ac143" stroke-width="1.6" stroke-dasharray="2 3"/>
    <circle cx="29" cy="30" r="4" fill="none" stroke="#7ac143" stroke-width="2.4"/>
    <line x1="32" y1="29" x2="46" y2="24" stroke="#7ac143" stroke-width="2.4"/>
    <line x1="22" y1="42" x2="36" y2="42" stroke="#7ac143" stroke-width="2.4"/>
    <line x1="24" y1="47" x2="34" y2="47" stroke="#7ac143" stroke-width="2.4"/>
  </svg>
  <p class="abs feature" style="left:296px;top:30px"><b>Our FASTEST</b><br>Speed</p>

  <svg class="abs" style="left:31px;top:122px" width="50" height="38" viewBox="0 0 50 38" aria-hidden="true">
    <path d="M8 28 Q8 8 25 8 Q42 8 42 28" fill="none" stroke="#7ac143" stroke-width="2.6"/>
    <path d="M19 28 V4 H31 V28 M25 4 V24" fill="none" stroke="#7ac143" stroke-width="2.4"/>
    <path d="M2 29 H48 Q48 35 25 35 Q2 35 2 29 Z" fill="none" stroke="#7ac143" stroke-width="2.6" stroke-linejoin="round"/>
  </svg>
  <p class="abs feature" style="left:88px;top:113px"><span class="feature--caps">SPECIAL PRICING</span><br>During Construction</p>

  <div class="abs homes" role="img" aria-label="Green glass house models with a fiber optic cable"></div>
  <div class="abs brand-small">
    <span class="brand-small__name">Lumen Path</span>
    <span class="brand-small__dot"></span>
  </div>

  <div class="abs offer" style="left:68px;top:219px"><span class="offer__big">$60/</span><span class="offer__small">MONTH</span></div>
  <div class="abs mascot" role="img" aria-label="Cartoon character with arms raised holding wifi signals" style="left:249px;top:216px;height:144px"></div>
  <div class="abs offer" style="left:373px;top:219px"><span class="offer__big">10</span><span class="offer__small">GIGS</span></div>

  <div class="abs cta" style="top:368px">
    <span class="cta__url">lumenpath.net</span>
    <span class="cta__button">SIGN UP TODAY!</span>
  </div>
</section>

</body>
</html>
```